Coffee bag stamp design for new coffee brand

Stamp design that will be used like a label on a coffee package.
It must be a vector that can be produced as a stamp. Coffee bag is from brown craft paper. I upload image of this bag. Size of design is 80mm x 140mm.
I also uploaded two pictures for inspiration, but I will also appreciate new ideas.

Target Market(s)

Coffee lovers, who love to try new coffee. Also hipsters.

Colors

Designer to choose only greyscale colors for use in the design.

Requirements
Must have
• Some information about coffee must have:
Name: BRAZIL (the biggest font in that design)
Region: Santos
Altitude: 60 – 1200 m.n.m.
Variety: Arabica
Processing: unwashed

```html
<!DOCTYPE html>
<html lang="en">
<head>
<meta charset="utf-8">
<title>Veluna Coffee – Brazil label</title>
<link rel="stylesheet" href="https://fonts.googleapis.com/css2?family=Bebas+Neue&family=Oswald:wght@300;500&family=Josefin+Sans:wght@700&display=swap">
<style>
  :root {
    --kraft: #c39e7f;
    --kraft-shade: #b48e6f;
    --ink: #333132;
    --ink-soft: #4a4647;
  }
  * { box-sizing: border-box; margin: 0; padding: 0; }
  html, body {
    width: 935px; height: 1200px; overflow: hidden;
    background: var(--kraft);
  }
  .label {
    position: absolute; left: 157px; top: 50px;
    width: 620px; height: 1100px;
    color: var(--ink);
  }
  .foliage {
    position: absolute;
    background: linear-gradient(180deg, rgba(51,49,50,0.28), rgba(51,49,50,0.16));
    border-radius: 6px;
  }
  .foliage--crown { left: 10px; top: 0; width: 600px; height: 210px; }
  .foliage--left { left: 0; top: 230px; width: 80px; height: 330px; }
  .foliage--right { right: 0; top: 230px; width: 80px; height: 330px; }
  .foliage--base { left: 30px; top: 560px; width: 560px; height: 90px; }

  .brand {
    position: absolute; left: 100px; top: 262px; width: 420px; height: 280px;
    display: flex; flex-direction: column; align-items: center; justify-content: center;
    gap: 10px;
    font-family: "Josefin Sans", sans-serif; font-weight: 700;
    font-size: 62px; line-height: 1; letter-spacing: 3px; text-transform: uppercase;
    color: var(--ink); text-align: center;
  }
  .brand__dot {
    width: 40px; height: 40px; border-radius: 50%;
    background: var(--ink); flex: none; margin-bottom: 14px;
  }
  .brand__line { display: block; }

  .origin {
    position: absolute; left: 0; top: 650px; width: 620px; height: 220px;
  }
  .origin svg { position: absolute; inset: 0; }
  .origin__name {
    position: absolute; inset: 0;
    display: flex; align-items: center; justify-content: center;
    font-family: "Bebas Neue", sans-serif; font-weight: 400; font-size: 200px;
    letter-spacing: 6px; line-height: 1; padding-top: 18px;
    color: var(--kraft);
  }

  .specs {
    position: absolute; left: 0; top: 890px; width: 620px; height: 150px;
    font-family: "Oswald", sans-serif; font-size: 27px;
  }
  .specs__rule {
    position: absolute; left: 0; width: 620px; height: 2px; background: var(--ink);
  }
  .specs__divider {
    position: absolute; width: 2px; height: 75px; background: var(--ink);
  }
  .spec {
    position: absolute; height: 75px; display: flex; align-items: center;
    white-space: nowrap;
  }
  .spec__key { font-weight: 300; text-transform: uppercase; font-size: 24px; }
  .spec__value { font-weight: 500; margin-left: 6px; }

  .seal {
    position: absolute; left: 200px; top: 1060px; width: 220px; height: 36px;
    background: rgba(51,49,50,0.3); border-radius: 18px;
  }
</style>
</head>
<body>
  <main class="label">
    <div class="foliage foliage--crown" role="img" aria-label="Hand-drawn coffee leaf branches across the top"></div>
    <div class="foliage foliage--left" role="img" aria-label="Coffee leaf sprigs along the left edge"></div>
    <div class="foliage foliage--right" role="img" aria-label="Coffee leaf sprigs along the right edge"></div>

    <div class="brand">
      <span class="brand__dot"></span>
      <span class="brand__line">Veluna</span>
      <span class="brand__line">Coffee</span>
    </div>

    <div class="foliage foliage--base" role="img" aria-label="Small leaf sprigs above the origin banner"></div>

    <section class="origin">
      <svg width="620" height="220" viewBox="0 0 620 220" aria-hidden="true">
        <path fill="var(--ink)" d="M0 14 q10 -14 20 0 t20 0 t20 0 t20 0 t20 0 t20 0 t20 0 t20 0 t20 0 t20 0 t20 0 t20 0 t20 0 t20 0 t20 0 t20 0 t20 0 t20 0 t20 0 t20 0 t20 0 t20 0 t20 0 t20 0 t20 0 t20 0 t20 0 t20 0 t20 0 t20 0 t20 0 L620 206 q-10 14 -20 0 t-20 0 t-20 0 t-20 0 t-20 0 t-20 0 t-20 0 t-20 0 t-20 0 t-20 0 t-20 0 t-20 0 t-20 0 t-20 0 t-20 0 t-20 0 t-20 0 t-20 0 t-20 0 t-20 0 t-20 0 t-20 0 t-20 0 t-20 0 t-20 0 t-20 0 t-20 0 t-20 0 t-20 0 t-20 0 t-20 0 Z"/>
      </svg>
      <h1 class="origin__name">Brazil</h1>
    </section>

    <section class="specs">
      <div class="specs__rule" style="top:0"></div>
      <div class="specs__rule" style="top:74px"></div>
      <div class="specs__rule" style="top:148px"></div>
      <div class="specs__divider" style="left:215px; top:0"></div>
      <div class="specs__divider" style="left:255px; top:74px"></div>

      <div class="spec" style="left:6px; top:0"><span class="spec__key">Region:</span><span class="spec__value">Santos</span></div>
      <div class="spec" style="left:232px; top:0"><span class="spec__key">Altitude:</span><span class="spec__value">60 – 1200 m.n.m.</span></div>
      <div class="spec" style="left:36px; top:74px"><span class="spec__key">Variety:</span><span class="spec__value">Arabica</span></div>
      <div class="spec" style="left:272px; top:74px"><span class="spec__key">Processing:</span><span class="spec__value">Unwashed</span></div>
    </section>

    <div class="seal" role="img" aria-label="Small coffee bean flanked by two leaves"></div>
  </main>
</body>
</html>
```